Premium Juice and Wine Bottle Label

We require a premium label design for a Burgundy style wine bottle - the design should reflect pure and organic theme, with a reference to New Zealand blueberries. The winning design will look high-end, simple but sophisticated. Our logo is attached, refer :

https://www.orvalecellars.co.nz and https://www.pirovane.co.nz/wines/details/coming-soon-showcase/2018

for inspiration.

Target Market(s)

High-end retail grocery stores, wine shops, bars.

Requirements
Must have
• Label should leave enough space for barcode and nutrients/ingredients etc. Reference to New Zealand, natural-beverage, be very high-end in design. Refer links in project description for inspiration. Refer to attached logo, which must be used - feel free to change colour in order to obtain the best high-class design.
Nice to have
• N/A.
Should not have
• Cartoons or pictures of berries.

```html
<!DOCTYPE html>
<html lang="en">
<head>
<meta charset="utf-8">
<title>Kestrel Lane – New Zealand Natural Beverage Label</title>
<link rel="stylesheet" href="https://fonts.googleapis.com/css2?family=Playfair+Display:wght@400;700&family=Montserrat:wght@300;400&display=swap">
<style>
  :root {
    --paper: #ffffff;
    --ink: #111111;
    --label-ground: #f3f5f6;
    --pattern-tone: #e6eaec;
    --sky-pink: #e4b9c9;
    --sky-blue: #3f86c9;
    --peak-white: #e9eef5;
    --mountain-blue: #2a4aa0;
    --lake-blue: #2f9bd0;
    --hill-gold: #b59a4a;
    --forest: #24351f;
    --gold-light: #fde7b0;
    --gold-deep: #f2a83a;
  }
  * { box-sizing: border-box; margin: 0; padding: 0; }
  html, body {
    width: 1200px;
    height: 1000px;
    overflow: hidden;
    background: var(--paper);
  }
  .canvas {
    position: relative;
    width: 1200px;
    height: 1000px;
    background: var(--paper);
    overflow: hidden;
  }
  .label {
    position: absolute;
    left: 51px;
    top: 239px;
    width: 587px;
    height: 584px;
    background: var(--label-ground);
  }
  .label-art {
    position: absolute;
    inset: 0;
    width: 587px;
    height: 584px;
  }
  .brand-name {
    position: absolute;
    left: 0;
    width: 100%;
    top: 358px;
    display: flex;
    justify-content: center;
    align-items: center;
    gap: 10px;
    font-family: "Playfair Display", serif;
    font-weight: 700;
    font-size: 38px;
    color: var(--ink);
  }
  .brand-mark {
    width: 14px;
    height: 14px;
    background: var(--ink);
  }
  .origin {
    position: absolute;
    left: 0;
    width: 100%;
    top: 423px;
    text-align: center;
    font-family: "Playfair Display", serif;
    font-weight: 700;
    font-size: 15px;
    color: var(--ink);
  }
  .category {
    position: absolute;
    left: 0;
    width: 100%;
    top: 444px;
    text-align: center;
    font-family: "Montserrat", sans-serif;
    font-weight: 400;
    font-size: 12px;
    letter-spacing: 4px;
    color: var(--ink);
  }
  .info-space {
    position: absolute;
    left: 0;
    width: 100%;
    top: 501px;
    text-align: center;
    font-family: "Montserrat", sans-serif;
    font-weight: 300;
    font-size: 14px;
    color: var(--ink);
  }
  .side-title, .side-subtitle {
    position: absolute;
    white-space: nowrap;
    color: var(--ink);
    transform: translate(-50%, -50%) rotate(-90deg);
  }
  .side-title {
    left: 1006px;
    top: 508px;
    font-family: "Playfair Display", serif;
    font-weight: 400;
    font-size: 112px;
    line-height: 1;
  }
  .side-subtitle {
    left: 1095px;
    top: 507px;
    font-family: "Montserrat", sans-serif;
    font-weight: 300;
    font-size: 46px;
    letter-spacing: 9px;
    line-height: 1;
  }
</style>
</head>
<body>
<main class="canvas">
  <section class="label">
    <svg class="label-art" viewBox="0 0 587 584" xmlns="http://www.w3.org/2000/svg">
      <defs>
        <linearGradient id="landscape-tone" x1="0" y1="0" x2="0" y2="1">
          <stop offset="0" stop-color="var(--sky-pink)"/>
          <stop offset="0.2" stop-color="var(--sky-blue)"/>
          <stop offset="0.4" stop-color="var(--peak-white)"/>
          <stop offset="0.55" stop-color="var(--mountain-blue)"/>
          <stop offset="0.75" stop-color="var(--lake-blue)"/>
          <stop offset="0.9" stop-color="var(--hill-gold)"/>
          <stop offset="1" stop-color="var(--forest)"/>
        </linearGradient>
        <linearGradient id="gold-band" x1="0" y1="0" x2="1" y2="0">
          <stop offset="0" stop-color="var(--gold-deep)"/>
          <stop offset="0.3" stop-color="var(--gold-light)"/>
          <stop offset="0.7" stop-color="var(--gold-light)"/>
          <stop offset="1" stop-color="var(--gold-deep)"/>
        </linearGradient>
      </defs>
      <rect class="pattern-field" x="0" y="260" width="587" height="324" fill="var(--pattern-tone)" opacity="0.45" role="img" aria-label="Soft ornamental floral pattern across the lower label"/>
      <polygon class="gold-chevron" points="0,268 293,372 587,268 587,282 293,386 0,282" fill="url(#gold-band)"/>
      <polygon class="landscape" points="0,0 587,0 587,268 293,372 0,268" fill="url(#landscape-tone)" role="img" aria-label="Photograph of snow-capped alpine peaks above a turquoise lake with a road through golden hills"/>
    </svg>
    <div class="brand-name"><span class="brand-mark"></span>Kestrel Lane</div>
    <p class="origin">NEW ZEALAND</p>
    <p class="category">NATURAL-BEVERAGE</p>
    <p class="info-space">BARCODE AND NUTRIENTS/INGREDIENTS</p>
  </section>
  <p class="side-title">NEW ZEALAND</p>
  <p class="side-subtitle">NATURAL-BEVERAGE</p>
</main>
</body>
</html>
```